BPRV Postcard Design: Mosquito Control, Lawn Maintenance and Pressure washing

I have a new company based in Atlanta,Georgia named Brightwell Pest Relief Ventures, LLC. We specializes in Mosquito Control. We also have additional services: Lawn maintenance, Pressure Washing and Gutter Cleaning. I would like to see designs with the colors Black, Red, Gray. We would like the customer to think of us when it comes to Enjoying a mosquito free yard and improving the look and feel of their home and lawn.

Industry/Entity Type

It Company

Requirements
Nice to have
• Treatment plans starting at $69/mt - front of card
• The additional services we offer - back of card.

```html
<!DOCTYPE html>
<html lang="en">
<head>
<meta charset="utf-8">
<title>BPRV Postcard</title>
<link href="https://fonts.googleapis.com/css2?family=Alfa+Slab+One&family=Lato:wght@400;700&display=swap" rel="stylesheet">
<style>
  :root{
    --red:#d3202f;
    --red-dark:#a8121f;
    --black:#1d1d1d;
    --charcoal:#333333;
    --gray:#e9e9e9;
    --white:#ffffff;
    --line:#8a8a8a;
  }
  *{margin:0;padding:0;box-sizing:border-box}
  html,body{width:924px;height:1200px;overflow:hidden}
  body{background:var(--gray);position:relative;font-family:"Lato",sans-serif}
  .card{position:absolute;overflow:hidden;background:var(--white);box-shadow:0 2px 6px rgba(0,0,0,.18)}
  .card svg{position:absolute;left:0;top:0;display:block}
  .card-front{left:82px;top:71px;width:764px;height:495px}
  .card-back{left:82px;top:628px;width:770px;height:499px}

  .headline{position:absolute;left:455px;top:28px;width:300px;text-align:center;font-family:"Alfa Slab One",serif;line-height:1.02}
  .headline .light{display:block;color:var(--white);font-size:36px}
  .headline .strong{display:block;color:#111;font-size:46px;margin-top:2px}

  .brand-name{position:absolute;left:30px;top:328px;width:350px;text-align:center;font-family:"Alfa Slab One",serif;color:var(--red);font-weight:400;line-height:1.05}
  .brand-name .primary{display:block;font-size:50px}
  .brand-name .secondary{display:block;font-size:19px;margin-top:4px}

  .services{position:absolute;left:37px;top:318px;width:380px;color:var(--white)}
  .services h2{font-family:"Alfa Slab One",serif;font-weight:400;font-size:29px;letter-spacing:.5px;margin-bottom:10px}
  .services ul{list-style:none;display:grid;grid-template-columns:176px 180px;row-gap:8px;padding-left:10px}
  .services li{font-size:16.5px;position:relative;padding-left:12px}
  .services li::before{content:"";position:absolute;left:0;top:8px;width:6px;height:6px;border-radius:50%;background:var(--red)}

  .stamp-box{position:absolute;left:668px;top:27px;width:61px;height:61px;border:1.5px solid var(--black)}
  .address-line{position:absolute;left:470px;width:256px;height:0;border-top:1px solid var(--line)}
</style>
</head>
<body>

<section class="card card-front">
  <svg width="764" height="495" viewBox="0 0 764 495">
    <defs>
      <linearGradient id="whiteFade" x1="0" y1="0" x2="0" y2="1">
        <stop offset="0" stop-color="#ffffff"/><stop offset="1" stop-color="#e4e4e4"/>
      </linearGradient>
      <linearGradient id="lawnTones" x1="0" y1="0" x2="0" y2="1">
        <stop offset="0" stop-color="#4e3429"/><stop offset=".45" stop-color="#6b5a4a"/><stop offset=".6" stop-color="#6fa33f"/><stop offset="1" stop-color="#4f8a2a"/>
      </linearGradient>
      <linearGradient id="redPanel" x1="0" y1="0" x2="1" y2="1">
        <stop offset="0" stop-color="#e32a36"/><stop offset="1" stop-color="var(--red-dark)"/>
      </linearGradient>
      <radialGradient id="fogTones" cx=".55" cy=".5" r=".6">
        <stop offset="0" stop-color="#e8edf1"/><stop offset=".55" stop-color="#b7c2c8"/><stop offset="1" stop-color="#4f6b3e"/>
      </radialGradient>
      <linearGradient id="washTones" x1="0" y1="0" x2="1" y2="1">
        <stop offset="0" stop-color="#b5aa95"/><stop offset="1" stop-color="#d8d2c4"/>
      </linearGradient>
    </defs>
    <rect width="764" height="495" fill="url(#whiteFade)"/>
    <path role="img" aria-label="Photo: man pulling weeds from a green lawn beside a wooden fence" d="M0,0 H470 V300 C330,270 170,230 0,205 Z" fill="url(#lawnTones)"/>
    <path d="M0,209 C170,234 330,274 470,304 L470,332 C330,304 170,262 0,240 Z" fill="var(--black)"/>
    <rect y="468" width="764" height="27" fill="var(--black)"/>
    <circle cx="800" cy="180" r="440" fill="var(--black)"/>
    <circle cx="800" cy="180" r="432" fill="var(--white)"/>
    <circle cx="800" cy="180" r="424" fill="url(#redPanel)"/>
    <circle cx="740" cy="580" r="372" fill="var(--red)"/>
    <circle cx="740" cy="580" r="362" fill="var(--white)"/>
    <circle role="img" aria-label="Photo: technician fogging a garden with a mosquito sprayer" cx="740" cy="580" r="356" fill="url(#fogTones)"/>
    <circle cx="395" cy="245" r="70" fill="var(--black)"/>
    <circle cx="395" cy="245" r="64" fill="var(--white)"/>
    <circle role="img" aria-label="Photo: pressure washing a concrete driveway" cx="395" cy="245" r="58" fill="url(#washTones)"/>
  </svg>

  <h1 class="headline">
    <span class="light">Enjoy a</span>
    <span class="light">mosquito</span>
    <span class="strong">Free yard</span>
  </h1>

  <div class="brand-name">
    <span class="primary">Brightwell</span>
    <span class="secondary">Pest Relief Ventures, LLC</span>
  </div>
</section>

<section class="card card-back">
  <svg width="770" height="499" viewBox="0 0 770 499">
    <defs>
      <linearGradient id="charcoalPanel" x1="0" y1="0" x2="0" y2="1">
        <stop offset="0" stop-color="#262626"/><stop offset=".6" stop-color="#3c3c3c"/><stop offset="1" stop-color="#1f1f1f"/>
      </linearGradient>
      <linearGradient id="mowerTones" x1="0" y1="0" x2="0" y2="1">
        <stop offset="0" stop-color="#5f9e35"/><stop offset="1" stop-color="#3f7f25"/>
      </linearGradient>
      <linearGradient id="deckTones" x1="0" y1="0" x2="1" y2="1">
        <stop offset="0" stop-color="#8c7a58"/><stop offset="1" stop-color="#c9b98e"/>
      </linearGradient>
    </defs>
    <rect width="770" height="499" fill="var(--white)"/>
    <path d="M378,0 Q538,250 378,499" fill="none" stroke="var(--red)" stroke-width="5"/>
    <path d="M0,0 H360 Q520,250 360,499 H0 Z" fill="url(#charcoalPanel)"/>
    <circle cx="120" cy="112" r="205" fill="var(--white)"/>
    <circle cx="120" cy="112" r="198" fill="var(--red)"/>
    <circle cx="120" cy="112" r="186" fill="var(--white)"/>
    <circle role="img" aria-label="Photo: worker riding a red lawn mower across green grass" cx="120" cy="112" r="180" fill="url(#mowerTones)"/>
    <circle cx="290" cy="178" r="72" fill="var(--black)"/>
    <circle cx="290" cy="178" r="66" fill="var(--white)"/>
    <circle role="img" aria-label="Photo: pressure washer wand cleaning a wooden deck" cx="290" cy="178" r="60" fill="url(#deckTones)"/>
  </svg>

  <div class="services">
    <h2>WE SPECIALIZES IN</h2>
    <ul>
      <li>Mosquito Control</li>
      <li>Pressure Washing</li>
      <li>Lawn maintenance</li>
      <li>Gutter Cleaning</li>
    </ul>
  </div>

  <div class="stamp-box"></div>
  <div class="address-line" style="top:115px"></div>
  <div class="address-line" style="top:153px"></div>
  <div class="address-line" style="top:190px"></div>
</section>

</body>
</html>
```